Web Site Design

We need to design the whole web site for our small start up. We sell hospitality and culinary art internships abroad. I did my own design with WIX which is horrible meanwhile I started with my business. You can see it www.brightvoyage-intern.example I will need you to create a new and attractive web site and to leave it working on wix. The internship destinations are United Arab Emirates, Thailand, China, Spain, Brazil and maybe leave a couple of pages for future destinations.You could also get other ideas of other sites that do internships.

Target Market(s)

Students and recent graduates of hospitality and culinary art majors

Industry/Entity Type

Education

Number of Pages Required

5+ page

Requirements
Must have
• Addittional to our program destinations, or to the pages in the current site. The website must contain a page for Universities or Hotels who require our service

```html
<!DOCTYPE html>
<html lang="en">
<head>
<meta charset="utf-8">
<title>Hospitality Internships</title>
<link rel="stylesheet" href="https://fonts.googleapis.com/css2?family=Josefin+Sans:wght@400;600&family=EB+Garamond:wght@400&display=swap">
<style>
:root{
  --white:#ffffff;
  --ink:#2f2a28;
  --nav-ink:#2a2a2a;
  --overlay:rgba(40,30,28,.62);
  --pink:#dcc3b8;
  --pink-light:#e4cfc6;
  --pink-text:#6e5550;
  --heading:#3b302d;
  --footer:#342927;
  --footer-text:#f2ece9;
}
*{margin:0;padding:0;box-sizing:border-box}
html,body{width:1200px;height:3025px;overflow:hidden}
body{position:relative;background:var(--white);font-family:"EB Garamond",Georgia,serif;color:var(--ink)}
h1,h2,h3,h4{font-weight:400}
.abs{position:absolute}

/* navigation */
.site-nav{left:0;top:0;width:1200px;height:75px;background:var(--white)}
.site-nav ul{list-style:none;position:absolute;left:490px;top:26px;display:flex}
.site-nav li{font-family:"Josefin Sans",Arial,sans-serif;font-size:18px;letter-spacing:.5px;color:var(--nav-ink);margin-right:32px}
.site-nav li:nth-child(3){margin-right:18px}

/* hero */
.hero{left:0;top:75px;width:1200px;height:641px;background:linear-gradient(90deg,#5a3a2c 0%,#8a6a58 30%,#3a2a28 55%,#b8a49a 75%,#9a3a34 100%)}
.hero-caption{left:565px;top:288px;width:635px;height:186px;background:var(--overlay);color:var(--white);padding:22px 12px}
.hero-title{font-family:"Josefin Sans",Arial,sans-serif;font-size:40px;line-height:50px}
.hero-sub{font-family:"Josefin Sans",Arial,sans-serif;font-size:25px;letter-spacing:1px;margin-top:4px}

/* feature band */
.feature{left:0;top:726px;width:1200px;height:680px;background:linear-gradient(180deg,#3a1c16 0%,#6a2e24 10%,#2a1412 20%,#2a1412 85%,#8a1e1a 92%,#5a2a24 100%)}
.feature-inner{left:0;top:861px;width:1200px;height:440px;background:linear-gradient(90deg,rgba(20,12,10,.85),rgba(45,25,20,.75))}
.feature-title{left:20px;top:888px;font-family:"Josefin Sans",Arial,sans-serif;font-size:40px;color:var(--white);letter-spacing:1px}
.feature-text{left:22px;top:948px;width:525px;font-size:19.5px;line-height:29.5px;color:var(--footer-text)}
.read-more{left:418px;top:1195px;font-family:"Josefin Sans",Arial,sans-serif;font-size:18px;font-weight:600;color:var(--white);letter-spacing:.5px}
.feature-photo{left:585px;top:894px;width:537px;height:373px;background:linear-gradient(135deg,#6a5040 0%,#c8b8a8 45%,#e8e2dc 60%,#7a5a44 100%)}

/* info columns */
.info{left:0;top:1406px;width:1200px;height:520px;background:var(--pink)}
.info-photo{left:585px;top:1406px;width:615px;height:520px;background:linear-gradient(90deg,#d8c0b4 0%,#cdb3a6 50%,#bea195 100%)}
.h-section{font-family:"Josefin Sans",Arial,sans-serif;font-size:36px;color:var(--heading);letter-spacing:1px}
.h-sub{font-family:"Josefin Sans",Arial,sans-serif;font-size:24px;color:var(--heading);letter-spacing:.5px}
.copy{font-size:18.5px;line-height:27px;color:var(--pink-text);width:520px}

/* expertise */
.expertise{left:0;top:1926px;width:1200px;height:575px;background:var(--pink-light)}
.expertise-photo{left:16px;top:2055px;width:539px;height:369px;background:linear-gradient(180deg,#3a6ab8 0%,#c89a58 35%,#e8b868 55%,#3a2e2a 100%)}
.quote{left:625px;top:2295px;font-size:24px;line-height:45.5px;color:var(--heading)}

/* footer */
.site-footer{left:0;top:2525px;width:1200px;height:500px;background:var(--footer);color:var(--footer-text)}
.f-head{position:absolute;top:82px;font-family:"Josefin Sans",Arial,sans-serif;font-size:25px;color:var(--white);letter-spacing:.5px}
.f-about{position:absolute;left:24px;top:165px;width:255px;font-size:14px;line-height:18.5px;color:var(--footer-text)}
.f-list{position:absolute;list-style:none;top:160px;font-size:19.5px;line-height:35.7px;color:var(--footer-text)}
.f-contact{position:absolute;left:948px;top:158px;width:232px;font-size:19.5px;line-height:28.5px;font-style:normal;color:var(--footer-text)}
</style>
</head>
<body>

<nav class="site-nav abs">
  <ul>
    <li>HOME</li><li>SERVICES</li><li>DESTINATIONS</li><li>ABOUT</li><li>CONTACT</li>
  </ul>
</nav>

<section class="hero abs" role="img" aria-label="Photo of smiling hotel receptionists at a front desk"></section>
<div class="hero-caption abs">
  <h1 class="hero-title">Hospitality internships<br>are our specialty!</h1>
  <p class="hero-sub">QUOD PERMITIT LUMEN</p>
</div>

<section class="feature abs" role="img" aria-label="Blurred restaurant interior background"></section>
<div class="feature-inner abs"></div>
<h2 class="feature-title abs">ERIT NIHIL</h2>
<p class="feature-text abs">Quisque tincidunt quam a porta sagittis. Etiam at urna dolor. Curabitur semper, arcu ut consequat sagittis, arcu purus venenatis est, et tristique nibh nibh porttitor odio. Nunc blandit ac ante in accumsan. Vestibulum ac tincidunt eros. Suspendisse elementum in nisi ut fringilla. Suspendisse tincidunt orci sit amet tellus porta placerat. Nunc sed turpis ullamcorper, cursus sapien a, placerat massa. Duis auctor eleifend est, et maximus est sagittis vel. In sit</p>
<span class="read-more abs">READ MORE</span>
<div class="feature-photo abs" role="img" aria-label="Photo of a waiter carrying wine glasses in a restaurant"></div>

<section class="info abs"></section>
<div class="info-photo abs" role="img" aria-label="Faded photo of a bright hotel room"></div>
<h2 class="h-section abs" style="left:16px;top:1517px">ETIAM AT QUOQUE</h2>
<p class="copy abs" style="left:16px;top:1580px">Quisque tincidunt quam a porta sagittis. Etiam at urna dolor. Curabitur semper, arcu ut consequat sagittis, arcu purus venenatis est, et tristique nibh nibh porttitor odio. Nunc blandit ac ante in accumsan. Vestibulum ac tincidunt eros. Suspendisse elementum in nisi ut fringilla. Suspendisse tincidunt orci sit amet tellus porta</p>
<h3 class="h-sub abs" style="left:16px;top:1745px">ET QUIQUE POTEST</h3>
<p class="copy abs" style="left:16px;top:1799px">Quisque tincidunt quam a porta sagittis. Etiam at urna dolor. Curabitur semper, arcu ut consequat sagittis, arcu purus venenatis est, et tristique nibh nibh porttitor odio. Nunc blandit ac ante in</p>
<h2 class="h-section abs" style="left:617px;top:1509px">PERCIT TUTA</h2>
<p class="copy abs" style="left:617px;top:1572px">Quisque tincidunt quam a porta sagittis. Etiam at urna dolor. Curabitur semper, arcu ut consequat sagittis, arcu purus venenatis est, et tristique nibh nibh porttitor odio. Nunc blandit ac ante in accumsan. Vestibulum ac tincidunt eros. Suspendisse elementum in nisi ut fringilla. Suspendisse tincidunt orci sit amet tellus porta</p>
<h3 class="h-sub abs" style="left:617px;top:1735px">ET COMPREHENDA</h3>
<p class="copy abs" style="left:617px;top:1789px">Quisque tincidunt quam a porta sagittis. Etiam at urna dolor. Curabitur semper, arcu ut consequat sagittis, arcu purus venenatis est, et tristique nibh nibh porttitor odio. Nunc blandit ac ante in</p>

<section class="expertise abs"></section>
<h2 class="h-section abs" style="left:24px;top:1975px;font-size:42px">OUR EXPERTISE</h2>
<div class="expertise-photo abs" role="img" aria-label="Photo of an illuminated hotel facade with a hotel sign"></div>
<h3 class="h-sub abs" style="left:625px;top:2100px">VULPUS ELIT</h3>
<p class="copy abs" style="left:625px;top:2158px">Quisque tincidunt quam a porta sagittis. Etiam at urna dolor. Curabitur semper, arcu ut consequat sagittis, arcu purus venenatis est, et tristique nibh nibh porttitor odio. Nunc blandit ac ante in</p>
<blockquote class="quote abs">“eternatitem magistima chose<br>perception randa quod vivendum<br>et se quanda scit...”</blockquote>

<footer class="site-footer abs">
  <p class="f-about">Phasellus vulputate et nisi a luctus. Curabitur vitae nunc viverra, fermentum dui in, vehicula velit. Pellentesque habitant morbi tristique senectus et netus et malesuada fames ac turpis egestas. Suspendisse lacinia commodo libero in vestibulum. Aenean mattis dictum felis, eu commodo arcu tincidunt nec. Fusce rhoncus eros sed ante pulvinar sagittis. Fusce facilisis</p>
  <h4 class="f-head" style="left:319px">SERVICES</h4>
  <ul class="f-list" style="left:314px">
    <li>Phasellus vulputate</li><li>Enisi a luctus.</li><li>Curabitur vitae nunc</li><li>Viverra, fermentum</li><li>Dui in, vehicula velit.</li><li>Pellentesque habitant</li><li>Senectus et netus et</li><li>Malesuada fames ac</li>
  </ul>
  <h4 class="f-head" style="left:611px">MORE LINKS</h4>
  <ul class="f-list" style="left:613px">
    <li>Phasellus vulputate</li><li>Enisi a luctus.</li><li>Curabitur vitae nunc</li><li>Viverra, fermentum</li><li>Dui in, vehicula velit.</li><li>Pellentesque habitant</li><li>Senectus et netus et</li><li>Malesuada fames ac</li>
  </ul>
  <h4 class="f-head" style="left:912px">CONTACT US</h4>
  <address class="f-contact">Address:<br>Phasellus vulputate et nisi a luctus. Curabitur vitae nunc viverra, fermentum dui in, vehicula velit. Pellentesque habitant morbi tristique senectus et netus et malesuada fames ac turpis egestas.</address>
</footer>

</body>
</html>
```